UK Supplement Company Needs a Label for Diet Protein Powder

We need a new, modern and fresh design for our Diet Protein Powder. Our protein powder is packaged in black plastic tubs (photo attached) and needs an attractive label. We would like to see designs that grab attention and look professional. We're very open to ideas. The label should be 88mm x 365mm. We also prefer PSD format where possible. These alterations could be made once your design is chosen. Have attached photo of our shake ingredients/benefits.
Updates

Need extra days to review

Target Market(s)

Slimmers

Industry/Entity Type

Health And Wellness

Font styles to use
Serif
Sans Serif

Colors

Designer to choose colors to be used in the design.

Requirements
Must have
• Clean, Modern and Professional Look. Eye catching. The flavour, we offer 6 flavours so this must be something we can edit (Flavours are Banana, Chocolate, Chocolate Mint, Strawberry, Toffee and Vanilla).
Nice to have
• Our logo, this can be VANTO Nutrition or just VANTO. Our logo files are attached.
Should not have
• We do not want to see people (faces or bodies) on the design.

```html
<!DOCTYPE html>
<html lang="en">
<head>
<meta charset="utf-8">
<title>VANTO Nutrition – Low Calorie Protein Shake Label</title>
<link rel="stylesheet" href="https://fonts.googleapis.com/css2?family=Anton&family=Exo+2:wght@400;600&family=Roboto+Condensed:wght@700&display=swap">
<style>
  :root {
    --page: #ffffff;
    --label-dark: #1d1e20;
    --label-mid: #2c2d30;
    --accent-blue: #2aa6e4;
    --accent-blue-dark: #0f6fa8;
    --silver: #e4e6e8;
    --silver-shade: #a9acb0;
    --white: #ffffff;
    --line: #d9dde1;
    --chocolate: #4a2a16;
  }
  html, body {
    margin: 0;
    padding: 0;
    width: 697px;
    height: 1200px;
    overflow: hidden;
    background: var(--page);
  }
  .canvas {
    position: relative;
    width: 697px;
    height: 1200px;
  }
  .label {
    position: absolute;
    left: 38px;
    top: 355px;
    width: 620px;
    height: 490px;
    overflow: hidden;
    background: radial-gradient(ellipse at 50% 40%, var(--label-mid), var(--label-dark) 75%);
  }
  .label-art {
    position: absolute;
    inset: 0;
  }
  .brand {
    position: absolute;
    top: 40px;
    left: 0;
    width: 100%;
    text-align: center;
    font-family: "Anton", sans-serif;
    font-size: 30px;
    line-height: 36px;
    letter-spacing: 1px;
    color: var(--white);
  }
  .headline {
    position: absolute;
    top: 94px;
    left: 0;
    width: 100%;
    margin: 0;
    text-align: center;
    font-family: "Anton", sans-serif;
    font-weight: 400;
    font-size: 60px;
    line-height: 66px;
    color: var(--silver);
    text-shadow: 0 2px 0 var(--silver-shade);
  }
  .headline span { display: block; }
  .headline .line-one { word-spacing: 14px; }
  .tagline {
    position: absolute;
    top: 240px;
    left: 125px;
    width: 370px;
    height: 30px;
    border-radius: 15px;
    background: var(--accent-blue);
    font-family: "Exo 2", sans-serif;
    font-weight: 600;
    font-size: 19px;
    line-height: 30px;
    letter-spacing: 1.5px;
    text-align: center;
    color: var(--label-dark);
  }
  .facts {
    position: absolute;
    top: 312px;
    left: 128px;
    width: 218px;
    border: 1px solid var(--accent-blue);
    font-family: "Roboto Condensed", sans-serif;
    color: var(--white);
  }
  .facts-calories {
    text-align: center;
    padding: 3px 0 2px;
    font-family: "Exo 2", sans-serif;
    font-size: 20px;
    letter-spacing: 1.5px;
    color: var(--accent-blue);
    line-height: 22px;
  }
  .per-serving {
    display: block;
    font-size: 9px;
    letter-spacing: 0.5px;
    color: var(--line);
    line-height: 11px;
  }
  .facts-grid {
    display: grid;
    grid-template-columns: 62fr 42fr 54fr 52fr;
    gap: 4px;
    padding: 4px;
  }
  .fact {
    border: 1px solid var(--line);
    text-align: center;
    padding: 3px 1px;
    font-size: 11px;
    line-height: 11px;
    min-height: 24px;
  }
  .fact small {
    display: block;
    font-size: 6.5px;
    line-height: 7px;
    font-weight: 400;
    font-family: "Exo 2", sans-serif;
  }
  .fact.big { font-size: 15px; line-height: 14px; }
  .carbs {
    position: absolute;
    top: 318px;
    left: 358px;
    font-family: "Exo 2", sans-serif;
    font-size: 20px;
    letter-spacing: 1.5px;
    color: var(--white);
    line-height: 22px;
  }
  .carbs .per-serving { text-align: center; }
  .flavour {
    position: absolute;
    top: 365px;
    left: 356px;
    display: flex;
    align-items: center;
    gap: 8px;
    font-family: "Roboto Condensed", sans-serif;
    font-size: 17px;
    color: var(--white);
  }
  .flavour-dot {
    width: 22px;
    height: 22px;
    border-radius: 50%;
    background: radial-gradient(circle at 40% 35%, #7a4a2a, var(--chocolate));
    border: 1px solid #141414;
  }
  .net-weight {
    position: absolute;
    top: 425px;
    left: 422px;
    width: 64px;
    height: 46px;
    border: 1.5px solid var(--line);
    border-radius: 5px;
    text-align: center;
    font-family: "Roboto Condensed", sans-serif;
    color: var(--white);
  }
  .net-weight strong {
    display: block;
    font-family: "Exo 2", sans-serif;
    font-weight: 600;
    font-size: 23px;
    color: var(--accent-blue);
    line-height: 28px;
  }
  .net-weight span { font-size: 9px; line-height: 12px; display: block; }
</style>
</head>
<body>
<main class="canvas">
  <section class="label">
    <svg class="label-art" width="620" height="490" viewBox="0 0 620 490" aria-hidden="true">
      <rect x="0" y="0" width="620" height="16" fill="var(--accent-blue)"/>
      <path d="M0 120 Q 300 30 620 70" fill="none" stroke="#3a3b3f" stroke-width="18" opacity="0.6"/>
      <path d="M0 385 Q 250 355 620 460 L620 490 L0 490 Z" fill="#353639"/>
      <path d="M0 395 Q 180 405 360 445 Q 200 420 0 420 Z" fill="var(--accent-blue)"/>
      <path d="M0 428 Q 200 430 350 470 Q 180 445 0 445 Z" fill="var(--accent-blue-dark)"/>
      <path d="M0 455 Q 220 455 620 480 L620 490 L0 490 Z" fill="#18191b"/>
    </svg>

    <div class="brand">VANTO</div>

    <h1 class="headline"><span class="line-one">LOW CALORIE</span><span>PROTEIN SHAKE</span></h1>

    <div class="tagline">DIET PROTEIN POWDER</div>

    <div class="facts">
      <div class="facts-calories">117 CALORIES<span class="per-serving">PER SERVING</span></div>
      <div class="facts-grid">
        <div class="fact">120 MG<small>GREEN TEA EXTRACT</small></div>
        <div class="fact big">21G<small>PROTEIN</small></div>
        <div class="fact">120MG<small>ACAI BERRY</small></div>
        <div class="fact">15MG<small>CLA POWDER</small></div>
      </div>
    </div>

    <div class="carbs">4.2 CARBS<span class="per-serving">PER SERVING</span></div>

    <div class="flavour"><span class="flavour-dot"></span>CHOCOLATE</div>

    <div class="net-weight"><strong>500</strong><span>GRAMMS</span></div>
  </section>
</main>
</body>
</html>
```